Book Cover - For Best Selling Diet

Hi
Book cover required for a diet book being marketed to become a best seller
For best quality, image will be 2820 pixels on the shortest side and 4500 pixels on the longest side .
The book name : Bright Morning Plan
By Corinna Plett
( will add in the extra text once we see design - top and bottom subtitle )
I do not want a photo of a person on the book.
PLEASE SEE " THE 9 STEP FRAME" by Ned Galbury as an example of solid style and I also love Quiet Ledger for the font.
Branding Colours:
#F26432
#A4195C
#A7D8CC
Font that runs through our brand is : helvetica neue
This is for a book that will be marketed for #1 bestseller - So please only quality
designs that are designed in a unique style.
Thanks
Target Market(s)
Busy Working Mums, Affluent, 30+ .
Look and feel

```html
<!DOCTYPE html>
<html lang="en">
<head>
<meta charset="utf-8">
<title>Bright Morning Plan — Cover Spread</title>
<link rel="stylesheet" href="https://fonts.googleapis.com/css2?family=Oswald:wght@400;600;700&family=Lato:wght@300;400&family=PT+Serif&display=swap">
<style>
  :root {
    --page: #e9e9ec;
    --brand-orange: #F26432;
    --brand-plum: #A4195C;
    --brand-mint: #A7D8CC;
    --purple-deep: #2a1f5c;
    --purple-soft: rgba(98, 82, 168, 0.78);
    --purple-band: rgba(92, 78, 160, 0.55);
    --sky: #efe6dc;
    --street: #6d5a86;
    --white: #ffffff;
    --watch-face: #f4f4f4;
  }
  * { box-sizing: border-box; margin: 0; padding: 0; }
  html, body { width: 1200px; height: 1000px; overflow: hidden; }
  body { background: var(--page); position: relative; font-family: "Lato", sans-serif; }

  .spread {
    position: absolute; left: 110px; top: 150px;
    width: 980px; height: 700px;
    display: flex;
    box-shadow: 0 10px 30px rgba(0,0,0,0.18);
  }
  .back, .front { position: relative; width: 450px; height: 700px; overflow: hidden; }
  .spine {
    position: relative; width: 80px; height: 700px; overflow: hidden;
    background: linear-gradient(180deg, #4a3c8c, #6a5cae);
  }

  .city-photo {
    position: absolute; inset: 0;
    background: linear-gradient(180deg, var(--sky) 0%, #b9a2b6 30%, #7d6799 55%, var(--street) 80%, #5b4a78 100%);
  }
  .back .city-photo {
    background: linear-gradient(180deg, #9b86b8 0%, #7d6aa4 40%, #5f4f8c 100%);
  }

  .stopwatch {
    position: absolute; border-radius: 50%;
    background: radial-gradient(circle, var(--watch-face) 0 62%, var(--brand-mint) 63% 100%);
    box-shadow: 0 4px 10px rgba(0,0,0,0.3);
  }

  /* back cover */
  .back-panel {
    position: absolute; left: 26px; top: 0; width: 170px; height: 700px;
    background: var(--purple-soft);
  }
  .back .stopwatch { left: 60px; top: 120px; width: 86px; height: 86px; }
  .back-copy {
    position: absolute; left: 40px; top: 270px; width: 144px;
    font-family: "PT Serif", serif; font-size: 9.5px; line-height: 1.55;
    color: rgba(255,255,255,0.85);
  }
  .back-copy p + p { margin-top: 12px; }
  .pull-quote {
    position: absolute; left: 210px; top: 90px; width: 220px;
    font-family: "Lato", sans-serif; font-weight: 300; font-size: 37px; line-height: 1.05;
    color: rgba(255,255,255,0.9); text-transform: uppercase; text-align: center;
  }
  .publisher-band {
    position: absolute; left: 0; bottom: 0; width: 450px; height: 84px;
    background: var(--purple-deep);
    display: flex; align-items: center; justify-content: center;
    font-family: "PT Serif", serif; font-size: 12px; letter-spacing: 4px; color: var(--white);
  }

  /* spine */
  .spine-title, .spine-author {
    position: absolute; left: 50%; white-space: nowrap; color: var(--white);
  }
  .spine-title {
    top: 180px; font-family: "Oswald", sans-serif; font-weight: 700; font-size: 28px; letter-spacing: 1px;
    transform: translate(-50%, -50%) rotate(90deg);
  }
  .spine-author {
    top: 560px; font-family: "PT Serif", serif; font-size: 13px; letter-spacing: 4px;
    transform: translate(-50%, -50%) rotate(90deg);
  }

  /* front cover */
  .front-author {
    position: absolute; top: 46px; left: 0; width: 450px; text-align: center;
    font-family: "Oswald", sans-serif; font-weight: 600; font-size: 28px; color: var(--brand-plum);
  }
  .front .stopwatch { left: 145px; top: 225px; width: 160px; height: 160px; }
  .title-band {
    position: absolute; left: 0; top: 330px; width: 450px; height: 120px;
    background: var(--purple-band);
  }
  .title {
    position: absolute; left: 0; top: 392px; width: 450px; text-align: center;
    font-family: "Oswald", sans-serif; font-weight: 700; text-transform: uppercase; line-height: 1;
    white-space: nowrap;
  }
  .title-lead { display: block; color: var(--white); font-size: 58px; text-align: left; padding-left: 40px; }
  .title-main { display: block; color: var(--brand-orange); font-size: 84px; margin-top: -4px; }
  .title-tail {
    display: flex; align-items: center; justify-content: center; gap: 12px;
    color: var(--white); font-size: 22px; font-weight: 400; margin-top: 6px; letter-spacing: 2px;
  }
  .title-tail::before, .title-tail::after { content: ""; width: 90px; height: 1px; background: rgba(255,255,255,0.8); }
</style>
</head>
<body>
  <main class="spread">
    <section class="back">
      <div class="city-photo" role="img" aria-label="Photograph of a city street lined with tall buildings, tinted purple"></div>
      <div class="back-panel"></div>
      <div class="stopwatch" role="img" aria-label="Illustration of a stopwatch"></div>
      <div class="back-copy">
        <p>Fifteen focused minutes each morning can reshape how you eat, move and rest. This plan fits real schedules and busy family routines without strict rules.</p>
        <p>Inside you will find simple meal ideas, quick shopping lists and gentle habits that build steady energy through the working day and into the evening.</p>
        <p>Start small, stay consistent and watch lasting change follow.</p>
      </div>
      <p class="pull-quote">Aenean quam, in sceleri sque sem at dolor. Maece-nas mattis.</p>
      <div class="publisher-band">LANTERNWAY PRESS</div>
    </section>

    <section class="spine">
      <span class="spine-title">BRIGHT MORNING PLAN</span>
      <span class="spine-author">CORINNA PLETT</span>
    </section>

    <section class="front">
      <div class="city-photo" role="img" aria-label="Photograph of a city street with tall buildings and a crosswalk, tinted purple"></div>
      <p class="front-author">CORINNA PLETT</p>
      <div class="title-band"></div>
      <div class="stopwatch" role="img" aria-label="Illustration of a stopwatch"></div>
      <h1 class="title">
        <span class="title-lead">Bright</span>
        <span class="title-main">Morning</span>
        <span class="title-tail">Plan</span>
      </h1>
    </section>
  </main>
</body>
</html>
```